Business Card Design needed for start up company Pelmora

In need of a new business card designed for a start up company based in Sydney, Pelmora is a new start up innovative Company, our mission it to make property accessible for everyday Australian and to become the leading Real Estate platform in Australia. We want it to be fresh and clean.

Industry/Entity Type

Financial

Contact Information for Business Card

Section for Name
Section for Title

PELMORA - Keys Within Reach
Mobile:
Direct:

Font styles to use
Sans Serif

Colors
33a6d7
0692cd
0255a3
ffffff

Requirements
Must have
• Logo, all business card details

```html
<!DOCTYPE html>
<html lang="en">
<head>
<meta charset="utf-8">
<title>Pelmora Business Card</title>
<link rel="stylesheet" href="https://fonts.googleapis.com/css2?family=Source+Sans+3:wght@400;600;700;800&display=swap">
<style>
  :root {
    --sky: #33a6d7;
    --sky-deep: #0692cd;
    --navy: #1d3b70;
    --royal: #0255a3;
    --white: #ffffff;
    --paper: #f4f4f3;
    --stage: #e9e8e6;
    --ink-navy: #1f3f78;
  }
  * { margin: 0; padding: 0; box-sizing: border-box; }
  html, body {
    width: 1200px; height: 960px; overflow: hidden;
    background: var(--stage);
    font-family: "Source Sans 3", Arial, sans-serif;
  }
  .canvas { position: relative; width: 1200px; height: 960px; }
  .card {
    position: absolute; width: 598px; height: 343px;
    border-radius: 18px; overflow: hidden;
    box-shadow: 0 3px 8px rgba(0,0,0,0.18);
  }
  .card-front { left: 217px; top: 131px; background: var(--paper); }
  .card-back { left: 381px; top: 504px; background: var(--sky); }
  .front-curve { position: absolute; inset: 0; }

  .brand { position: absolute; display: flex; align-items: center; }
  .brand-dot { border-radius: 50%; flex: none; }
  .brand-name { font-weight: 800; letter-spacing: -0.5px; line-height: 1; }

  .card-front .brand { left: 33px; top: 141px; }
  .card-front .brand-dot { width: 66px; height: 66px; background: var(--sky-deep); margin-right: 8px; }
  .card-front .brand-name { font-size: 42px; color: var(--ink-navy); }

  .contact { position: absolute; left: 370px; top: 86px; color: var(--white); }
  .contact-name { font-size: 21px; font-weight: 700; color: var(--sky); letter-spacing: 0.6px; line-height: 1; }
  .contact-title { font-size: 16px; margin-top: 4px; letter-spacing: 0.3px; }
  .contact-address { font-size: 14.5px; line-height: 18px; margin-top: 12px; }
  .contact-lines { list-style: none; margin-top: 11px; font-size: 14.5px; }
  .contact-lines li { display: flex; align-items: center; height: 19.5px; }
  .contact-lines svg { width: 13px; height: 13px; margin-right: 9px; flex: none; }

  .card-back .brand { left: 124px; top: 116px; }
  .card-back .brand-dot { width: 104px; height: 104px; background: var(--white); margin-right: 12px; }
  .card-back .brand-name { font-size: 64px; color: var(--white); }
  .tagline {
    position: absolute; left: 0; right: 0; top: 286px;
    text-align: center; color: var(--white); font-size: 16px;
  }
</style>
</head>
<body>
<main class="canvas">
  <section class="card card-front" aria-label="Business card front">
    <svg class="front-curve" width="598" height="343" viewBox="0 0 598 343" aria-hidden="true">
      <path d="M432,0 C250,45 222,300 462,343 L598,343 L598,0 Z" fill="var(--sky-deep)"/>
      <path d="M445,0 C272,42 240,300 472,343 L598,343 L598,0 Z" fill="var(--navy)"/>
    </svg>
    <div class="brand">
      <span class="brand-dot"></span>
      <span class="brand-name">PELMORA</span>
    </div>
    <div class="contact">
      <p class="contact-name">LIAM HARPER</p>
      <p class="contact-title">CEO/FOUNDER</p>
      <p class="contact-address">412 Wattle Street<br>Sydney, NSW 2000</p>
      <ul class="contact-lines">
        <li>
          <svg viewBox="0 0 16 16"><path d="M3.5 1.5l2.5 0 1.2 3.2-1.7 1.2c.8 1.8 2.2 3.2 4 4l1.2-1.7 3.2 1.2v2.5c0 .8-.7 1.5-1.5 1.5C6.9 13.4 2 8.5 2 3c0-.8.7-1.5 1.5-1.5z" fill="var(--sky)"/></svg>
          612 418 3029
        </li>
        <li>
          <svg viewBox="0 0 16 16"><rect x="4" y="1" width="8" height="14" rx="1.5" fill="none" stroke="var(--sky)" stroke-width="1.6"/><circle cx="8" cy="12.3" r="0.9" fill="var(--sky)"/></svg>
          745 219 6083
        </li>
        <li>
          <svg viewBox="0 0 16 16"><rect x="1" y="3.5" width="14" height="9" rx="1" fill="var(--sky)"/><path d="M1.5 4l6.5 5 6.5-5" fill="none" stroke="var(--navy)" stroke-width="1.2"/></svg>
          liam@pelmora.com
        </li>
        <li>
          <svg viewBox="0 0 16 16"><circle cx="8" cy="8" r="6.5" fill="var(--sky)"/><path d="M1.5 8h13M8 1.5c-2.5 2.5-2.5 10.5 0 13M8 1.5c2.5 2.5 2.5 10.5 0 13" fill="none" stroke="var(--navy)" stroke-width="1"/></svg>
          www.pelmora.com
        </li>
      </ul>
    </div>
  </section>

  <section class="card card-back" aria-label="Business card back">
    <div class="brand">
      <span class="brand-dot"></span>
      <span class="brand-name">PELMORA</span>
    </div>
    <p class="tagline">Keys Within Reach</p>
  </section>
</main>
</body>
</html>
```